An envelope for Housekeepers / The Velvet Lantern

Globally, 212 million people are employed in the hospitality industry. While many get commemorated for their work, there is one job that is often looked over.
Housekeepers hardly ever get told how great of a job they are doing.
Our company QuillbrookCo is seeking to empower housekeepers by allowing our guests to tip them through a cool envelope.
The plan :
- Create an envelope that has a message on it, which will incentivize our clientele to tip their housekeepers at check-out, and give housekeepers the credit they deserve for their hard work.
Example :
- "Humans do well by doing good" / "a thank you for your housekeeper"
What to do :
- Create an envelope based on the attached file. The white page titled "The Velvet Lantern" will be the front of the envelope (feel free to improve it but we really like the concept of it). The four blue pages will be the back pages of the envelope. Feel free to scour the web for quotes & embodying the same message of generosity.
We are really looking forward to seeing what kind of creative envelope you can conjure.
PS : remember that the goal with this envelope is to empower housekeepers & incentivize guests to tip them.
Target Market(s)
Travelers & housekeepers
Industry/Entity Type
Hospitality
Other font styles liked:
- Trebuchet, Times New Roman
Requirements
Must have
- Our project must have :
- - A white first page titled "The Velvet Lantern" is a must
- - You can improve it, but do not change the concept of it
- - Font : simple & easy to read
- - Color of back page : Teal
Nice to have
- Always keep in mind that this envelope is made to empower housekeepers.
Should not have
- Just keep it simple. Don't complicate things.

```html
<!DOCTYPE html>
<html lang="en">
<head>
<meta charset="utf-8">
<title>The Velvet Lantern – Housekeeper Envelope</title>
<link rel="stylesheet" href="https://fonts.googleapis.com/css2?family=Cinzel:wght@400;500&family=Tinos:wght@700&family=Montserrat:wght@500&display=swap">
<style>
  :root {
    --backdrop: #454545;
    --paper: #ffffff;
    --teal: #acdddd;
    --ink-light: #ffffff;
    --ink-grey: #555555;
  }
  html, body {
    margin: 0;
    padding: 0;
    width: 1189px;
    height: 1200px;
    overflow: hidden;
    background: var(--backdrop);
  }
  .canvas {
    position: relative;
    width: 1189px;
    height: 1200px;
  }
  .page {
    position: absolute;
    top: 148px;
    width: 508px;
    height: 903px;
    box-shadow: 2px 3px 6px rgba(0,0,0,0.45);
  }
  .page--front { left: 58px; background: var(--paper); }
  .page--back  { left: 620px; background: var(--teal); }

  .front-title {
    position: absolute;
    left: 0;
    right: 0;
    top: 508px;
    margin: 0;
    text-align: center;
    font-family: "Cinzel", serif;
    font-weight: 500;
    font-size: 55px;
    line-height: 60px;
    letter-spacing: 0.16em;
    color: var(--teal);
    text-transform: uppercase;
  }
  .front-title span { display: block; padding-left: 0.16em; }

  .brand-band {
    position: absolute;
    top: 805px;
    left: 0;
    right: 0;
    height: 49px;
  }
  .brand-band__bar {
    position: absolute;
    top: 0;
    height: 49px;
    background: var(--teal);
  }
  .brand-band__bar--left { left: 0; width: 135px; }
  .brand-band__bar--right { right: 0; width: 138px; }
  .brand-mark {
    position: absolute;
    left: 135px;
    width: 235px;
    top: 0;
    height: 49px;
    display: flex;
    align-items: center;
    justify-content: center;
    gap: 10px;
    font-family: "Montserrat", sans-serif;
    font-weight: 500;
    font-size: 21px;
    color: var(--ink-grey);
  }

  .back-quote {
    position: absolute;
    left: 0;
    right: 0;
    top: 345px;
    margin: 0;
    text-align: center;
    font-family: "Cinzel", serif;
    font-weight: 400;
    font-size: 31px;
    line-height: 36px;
    letter-spacing: 0.08em;
    color: var(--ink-light);
  }
  .back-quote span { display: block; }
  .back-tagline {
    position: absolute;
    left: 0;
    right: 0;
    top: 531px;
    margin: 0;
    text-align: center;
    font-family: "Tinos", serif;
    font-weight: 700;
    font-size: 17px;
    letter-spacing: 0.14em;
    color: var(--ink-light);
  }
</style>
</head>
<body>
<main class="canvas">
  <section class="page page--front" aria-label="Envelope front">
    <h1 class="front-title"><span>The</span><span>Velvet</span><span>Lantern</span></h1>
    <div class="brand-band">
      <div class="brand-band__bar brand-band__bar--left"></div>
      <div class="brand-mark">
        <svg width="30" height="30" viewBox="0 0 30 30" aria-hidden="true"><circle cx="15" cy="15" r="13" fill="none" stroke="var(--ink-grey)" stroke-width="3"/></svg>
        <span>QuillbrookCo</span>
      </div>
      <div class="brand-band__bar brand-band__bar--right"></div>
    </div>
  </section>

  <section class="page page--back" aria-label="Envelope back">
    <blockquote class="back-quote">
      <span>“Generosity</span>
      <span>isn’t an act.</span>
      <span>It’s a way of life.”</span>
      <span>Marlow Fenwick</span>
    </blockquote>
    <p class="back-tagline">A Thank You For Your Housekeeper</p>
  </section>
</main>
</body>
</html>
```